ATTORNEY FULL PAGE AD

We need a full page flyer for our law firm. We are sending it to people who were in an auto accident and injured. I want to let people know that by hiring an attorney that does not mean that they are suing someone. We will just help them in filing a claim and to get them compensated for: medical bills, lost wages, car repairs, future medical treatment or surgery, and pain/suffering. They will NOT have to pay us any money unless we get them paid. I want to show that we are compassionate to the fact that they went through this tramatic event that will effect their lives for ever. They do not have to worry about anything once they hire us. Our website is: www.brightwelllawfirm.com Our colors are black and gold. NO GAMBLING REFERENCES!!!!
Updates

Don't worry so much about content and wording. Once we get a design and images that look great we will message you the exact words we would like put into the paragraphs. The overall "look" and images are the most important. If anyone has a great change-up logo we are open to it as well. Thanks for everyone's hard work!

We like the dark colors. Some of the images are a little cheesy. We are a family business and treat are clients as family. I like the pictures o the car crashes an the hands. No blood. We want to come off as respectful and trustworthy. It's more about how we will care for them as family than getting them lots of money. 

Target Market(s)

People who were in major accidents and have serious injuries

Industry/Entity Type

Attorney

Requirements
Must have
• Must have our phone number: 1-855-MBRIGHT
Website: www.brightwelllawfirm.com
Company name: Brightwell Law Group
Attorney name: Morgan Ellis Brightwell
High gloss with card stock paper.
Classy - NOT cheesy
Should not have
• No cartoons. Very masculine and professional. There may have been death involved in the accident so we want the ad to be very compassionate and moving.

```html
<!DOCTYPE html>
<html lang="en">
<head>
<meta charset="utf-8">
<title>Brightwell Law Group – Injury Flyer</title>
<link href="https://fonts.googleapis.com/css2?family=Ubuntu:wght@300;400;700&display=swap" rel="stylesheet">
<style>
  :root {
    --backdrop: #3b3b3d;
    --sheet: #141416;
    --crimson: #ae1124;
    --crimson-text: #b8142a;
    --white: #ffffff;
    --ink-light: #f2f2f2;
    --logo-panel: #1f1f21;
    --logo-rule: #e8d21a;
    --photo-dark: #0d0d0d;
    --photo-mid: #8a8a8a;
    --photo-light: #d4d4d4;
  }
  * { margin: 0; padding: 0; box-sizing: border-box; }
  html, body {
    width: 1200px; height: 1000px; overflow: hidden;
    background: var(--backdrop);
    font-family: 'Ubuntu', sans-serif;
  }
  .flyer {
    position: absolute; left: 199px; top: 0;
    width: 800px; height: 1000px;
    background: var(--sheet);
    overflow: hidden;
  }
  .hero {
    position: absolute; left: 0; top: 0; width: 800px; height: 486px;
    background:
      radial-gradient(ellipse 200px 150px at 390px 290px, rgba(190,60,60,0.55), transparent 70%),
      radial-gradient(ellipse 420px 320px at 480px 200px, var(--photo-light), var(--photo-mid) 55%, var(--photo-dark) 100%);
  }
  .brand-box {
    position: absolute; left: 22px; top: 0; width: 178px; height: 139px;
    background: var(--logo-panel);
    border-right: 2px solid var(--logo-rule);
    border-bottom: 2px solid var(--logo-rule);
    display: flex; align-items: center; justify-content: center;
    text-align: center;
  }
  .brand-name {
    color: var(--white); font-weight: 400; font-size: 21px; line-height: 1.25;
    letter-spacing: 1px; text-transform: uppercase;
  }
  .headline {
    position: absolute; left: 0; width: 800px; text-align: center; line-height: 1;
    font-weight: 400;
  }
  .headline-question { top: 152px; left: 2px; font-size: 66px; color: var(--crimson-text); }
  .headline-answer { top: 228px; font-size: 50px; color: var(--white); }
  .fee-badge {
    position: absolute; left: 581px; top: 280px; width: 178px; height: 174px;
  }
  .fee-badge-text {
    position: absolute; left: 581px; top: 296px; width: 178px;
    text-align: center; color: var(--white); font-size: 16px; line-height: 20px;
  }
  .fee-badge-text strong { display: block; font-size: 24px; line-height: 32px; font-weight: 700; }
  .hero-tagline {
    position: absolute; left: 36px; top: 430px; color: var(--white); font-size: 16px;
  }
  .practice-band {
    position: absolute; left: 0; top: 486px; width: 800px; height: 73px;
    background: var(--crimson); color: var(--white);
    padding: 14px 36px 0; font-size: 16px; line-height: 21px;
  }
  .intro {
    position: absolute; left: 36px; top: 597px; width: 385px;
    color: var(--ink-light); font-size: 16px; line-height: 20px;
  }
  .intro p { margin-bottom: 20px; }
  .intro .claims { color: var(--crimson-text); }
  .team-photo {
    position: absolute; left: 528px; top: 602px; width: 218px; height: 144px;
    background: linear-gradient(180deg, #f4f4f4 0%, #e2e2e2 45%, #2c2c30 46%, #1c1c20 100%);
  }
  .contact {
    position: absolute; left: 529px; top: 798px; font-style: normal;
    color: var(--ink-light); font-size: 16px; line-height: 20px;
  }
  .contact .gap { margin-top: 20px; }
</style>
</head>
<body>
  <main class="flyer">
    <section class="hero" role="img" aria-label="Black and white close-up of hands holding an injured knee, with a soft red glow at the pain point"></section>

    <div class="brand-box">
      <span class="brand-name">Brightwell<br>Law Group</span>
    </div>

    <h1 class="headline headline-question">INJURED?</h1>
    <h2 class="headline headline-answer">WE CAN HELP.</h2>

    <svg class="fee-badge" viewBox="0 0 180 180" preserveAspectRatio="none" aria-hidden="true">
      <polygon fill="#ae1124" points="180,90 169.2,111.2 167.9,135 148,148 135,167.9 111.2,169.2 90,180 68.8,169.2 45,167.9 32,148 12.1,135 10.8,111.2 0,90 10.8,68.8 12.1,45 32,32 45,12.1 68.8,10.8 90,0 111.2,10.8 135,12.1 148,32 167.9,45 169.2,68.8"/>
    </svg>
    <p class="fee-badge-text">You will<strong>NOT</strong>have to pay us<br>any money<br>unless we<br>get them paid.</p>

    <p class="hero-tagline">You do not have to worry about anything once they hire us.</p>

    <p class="practice-band">Brightwell Law Group handles a wide variety of personal injury cases, including DUI, automobile accidents, medical malpractice and worker’s comp</p>

    <div class="intro">
      <p>The Brightwell Law Group is a personal injury law firm based in Savannah, Georgia. Our dedicated team of attorneys and staff is here to assist you with the following personal injury claims.</p>
      <p class="claims">Car accidents, big truck accidents, DUI injury accidents, motorcycle accident, pedestrian accident injury, passenger accident injury, worker’s compensation, medical malpractice, nursing home abuse, dog bite injury, hospital injury, dental injury, pharmaceutical injury and premise injury, as well as several other injury claims.</p>
      <p>If you decide on Brightwell Law Group to handle your personal injury claim, you pay no money out of your pocket unless we win your case. Call the Brightwell Law Group now for a free, informational consultation to discuss your personal injury claim.</p>
    </div>

    <div class="team-photo" role="img" aria-label="Group of five attorneys in dark suits standing together against a white background"></div>

    <address class="contact">
      <div>Brightwell Law Group</div>
      <div>Morgan Ellis Brightwell</div>
      <div>418 Harlow St.</div>
      <div>Savannah, GA 31401</div>
      <div class="gap">1-855-MBRIGHT</div>
      <div class="gap">www.brightwelllawfirm.com</div>
    </address>
  </main>
</body>
</html>
```